Business Cards and stationary for Home builder
Business Cards and stationary for Home builder - Construction
Professional
Marv T. Osko
Group Box 812 RR # 7 Saskatoon, Sk. S7N 5L2 CANADA
marv@quillforge.ca
quillforge.ca
Big Logo And: Crafting prairie homes since 1992 Hire carpenters to build your home

```html
<!DOCTYPE html>
<html lang="en">
<head>
<meta charset="utf-8">
<title>Quillforge Homes Stationery</title>
<link rel="stylesheet" href="https://fonts.googleapis.com/css2?family=Open+Sans:wght@400;600;800&display=swap">
<style>
  :root {
    --backdrop: #e9e4dc;
    --paper: #ffffff;
    --brand-green: #1f7a2e;
    --brand-dark: #14552a;
    --text-grey: #555555;
    --label-grey: #6b6359;
    --faint-top: #f4f8f3;
    --faint-bottom: #e3ede1;
    --rule-green: #3c9a3f;
  }
  * { margin: 0; padding: 0; box-sizing: border-box; }
  html, body { width: 1200px; height: 1094px; overflow: hidden; }
  body {
    background: var(--backdrop);
    font-family: "Open Sans", Arial, sans-serif;
    position: relative;
  }
  .sheet {
    position: absolute;
    background: var(--paper);
    box-shadow: 0 4px 14px rgba(0,0,0,0.18);
    overflow: hidden;
  }
  .wordmark {
    color: var(--brand-dark);
    font-weight: 800;
    line-height: 1;
    white-space: nowrap;
    display: inline-block;
  }
  .wordmark .name { display: block; text-transform: uppercase; letter-spacing: 0.5px; }
  .wordmark .sub { display: block; text-align: right; font-size: 0.62em; margin-top: 0.12em; }
  .caption {
    position: absolute;
    font-size: 13px;
    letter-spacing: 2.5px;
    font-variant: small-caps;
    color: var(--label-grey);
  }

  /* Business card front */
  .card-front { left: 41px; top: 334px; width: 293px; height: 174px; }
  .card-front .wordmark { position: absolute; left: 14px; top: 22px; font-size: 26px; }
  .card-front .contact {
    position: absolute; left: 16px; top: 90px;
    font-size: 7.5px; line-height: 10.5px; color: var(--text-grey);
  }
  .card-front .contact .dot {
    display: inline-block; width: 5px; height: 5px; border-radius: 50%;
    background: var(--brand-green); margin-right: 4px; vertical-align: 0;
  }
  .card-front .person {
    position: absolute; right: 14px; bottom: 18px;
    font-size: 10px; font-weight: 600; color: var(--text-grey);
  }
  .card-front .person-rule {
    position: absolute; right: 0; bottom: 13px; width: 110px; height: 2px;
    background: var(--rule-green);
  }

  /* Business card back */
  .card-back { left: 41px; top: 559px; width: 293px; height: 171px; }
  .card-back .wordmark { position: absolute; left: 14px; top: 36px; font-size: 30px; }
  .card-back .tagline {
    position: absolute; left: 0; right: 0; bottom: 28px; text-align: center;
    font-size: 10px; color: var(--brand-green);
  }

  /* Letterhead */
  .letterhead { left: 393px; top: 80px; width: 710px; height: 934px; }
  .letterhead .wordmark { position: absolute; left: 72px; top: 92px; font-size: 34px; }
  .letterhead .backdrop-art { position: absolute; left: 198px; top: 520px; }
  .letterhead .footer {
    position: absolute; left: 35px; bottom: 34px;
    font-size: 8.5px; line-height: 12px; color: var(--text-grey);
  }
  .letterhead .footer b { color: var(--brand-green); font-weight: 600; }
  .letterhead .tagline {
    position: absolute; right: 22px; bottom: 40px;
    font-size: 13px; color: var(--brand-green);
  }
</style>
</head>
<body>

  <section class="sheet card-front" aria-label="Business card front">
    <div class="wordmark"><span class="name">Quillforge</span><span class="sub">Homes</span></div>
    <div class="contact">
      Group Box 812 RR # 7<br>
      Saskatoon, Sk. S7N 5L2 CANADA<br>
      <span class="dot"></span>306-555-0142<br>
      <span class="dot"></span>306-555-0187<br>
      <span class="dot"></span>306-555-0163<br>
      <span class="dot"></span>marv@quillforge.ca<br>
      <span class="dot"></span>quillforge.ca
    </div>
    <div class="person">Marv T. Osko</div>
    <div class="person-rule"></div>
  </section>
  <div class="caption" style="left:100px; top:526px;">Business Card Front</div>

  <section class="sheet card-back" aria-label="Business card back">
    <div class="wordmark"><span class="name">Quillforge</span><span class="sub">Homes</span></div>
    <div class="tagline">Crafting prairie homes since 1992</div>
  </section>
  <div class="caption" style="left:104px; top:746px;">Business Card Back</div>

  <section class="sheet letterhead" aria-label="Letterhead">
    <svg class="backdrop-art" width="460" height="400" viewBox="0 0 460 400" role="img" aria-label="Faint background decoration area">
      <defs>
        <linearGradient id="faintFade" x1="0" y1="0" x2="0" y2="1">
          <stop offset="0" stop-color="var(--faint-top)"/>
          <stop offset="1" stop-color="var(--faint-bottom)"/>
        </linearGradient>
      </defs>
      <rect x="0" y="0" width="460" height="400" fill="url(#faintFade)"/>
    </svg>
    <div class="wordmark"><span class="name">Quillforge</span><span class="sub">Homes</span></div>
    <div class="footer">
      Group Box 812 RR # 7 Saskatoon, Sk. S7N 5L2 Canada<br>
      <b>Phone:</b> 306-555-0142 | <b>Cell:</b> 306-555-0187 | <b>Fax:</b> 306-555-0163<br>
      <b>Email:</b> marv@quillforge.ca | <b>www.quillforge.ca</b>
    </div>
    <div class="tagline">Crafting prairie homes since 1992</div>
  </section>

</body>
</html>
```